TRV PowerPoint

I am looking for a clean, corporate PowerPoint template.

I would like the following:
- title slide
- break slide
- blank slide with title (for graphs or graphics)
- an ending slide.

Target Market(s)

Business professionals, medium to large business clients.

Requirements
Must have
• Must incorporate the TRV logo in either the header or footer

```html
<!DOCTYPE html>
<html lang="en">
<head>
<meta charset="utf-8">
<title>Project Title here</title>
<link rel="stylesheet" href="https://fonts.googleapis.com/css2?family=Carlito:wght@400;700&family=Tinos:wght@700&display=swap">
<style>
  :root {
    --header-dark: #2a53b5;
    --header-light: #5d90f2;
    --header-end: #3a68d2;
    --header-rule: #1a2233;
    --footer-bg: #f3f3f3;
    --footer-rule: #3a6fd6;
    --brand-blue: #2f5597;
    --badge-blue: #3a6fd6;
    --slice-lightgray: #bfbfbf;
    --slice-midgray: #7f7f7f;
    --slice-darkgray: #595959;
    --slice-lightblue: #9dbcfb;
    --slice-midblue: #5b8ef0;
    --slice-deepblue: #3369d9;
    --hub-blue: #4a7be0;
    --text-dark: #111111;
    --white: #ffffff;
  }
  html, body {
    margin: 0;
    padding: 0;
    width: 1200px;
    height: 900px;
    overflow: hidden;
    background: var(--white);
  }
  .slide {
    position: relative;
    width: 1200px;
    height: 900px;
    overflow: hidden;
    background: var(--white);
  }
  .slide-header {
    position: absolute;
    left: 0; top: 0;
    width: 1200px;
    height: 92px;
    background: linear-gradient(90deg, var(--header-dark) 0%, var(--header-light) 62%, var(--header-end) 100%);
    border-bottom: 4px solid var(--header-rule);
  }
  .slide-title {
    position: absolute;
    left: 30px;
    top: 15px;
    margin: 0;
    font-family: "Tinos", "Times New Roman", serif;
    font-weight: 700;
    font-size: 51px;
    line-height: 1.2;
    color: var(--white);
  }
  .pie-chart {
    position: absolute;
    left: 0; top: 0;
  }
  .pie-slice { stroke: var(--white); stroke-width: 3; }
  .slice-label {
    font-family: "Carlito", "Calibri", sans-serif;
    font-weight: 700;
    font-size: 24px;
    text-anchor: middle;
  }
  .label-light { fill: var(--white); }
  .label-dark { fill: var(--text-dark); }
  .slide-footer {
    position: absolute;
    left: 0; bottom: 0;
    width: 1200px;
    height: 87px;
    background: var(--footer-bg);
    border-top: 3px solid var(--footer-rule);
  }
  .footer-brand {
    position: absolute;
    left: 20px;
    top: 16px;
    font-family: "Carlito", "Calibri", sans-serif;
    font-weight: 700;
    font-size: 46px;
    line-height: 1.1;
    color: var(--brand-blue);
  }
  .copyright {
    position: absolute;
    left: 894px;
    top: 31px;
    font-family: "Carlito", "Calibri", sans-serif;
    font-size: 22.5px;
    color: var(--text-dark);
  }
  .page-number {
    position: absolute;
    left: 1095px;
    top: 15px;
    width: 60px;
    height: 60px;
    border-radius: 50%;
    background: var(--badge-blue);
    color: var(--white);
    font-family: "Carlito", "Calibri", sans-serif;
    font-weight: 700;
    font-size: 23px;
    line-height: 60px;
    text-align: center;
  }
</style>
</head>
<body>
<main class="slide">
  <header class="slide-header">
    <h1 class="slide-title">Project Title here</h1>
  </header>

  <svg class="pie-chart" width="1200" height="900" viewBox="0 0 1200 900" aria-label="Pie chart with six segments">
    <path class="pie-slice" fill="var(--slice-lightgray)" d="M622 472 L622 177 A295 295 0 0 1 795.4 233.3 Z"/>
    <path class="pie-slice" fill="var(--slice-lightblue)" d="M622 472 L795.4 233.3 A295 295 0 0 1 899.2 572.9 Z"/>
    <path class="pie-slice" fill="var(--slice-midblue)" d="M622 472 L899.2 572.9 A295 295 0 0 1 727.7 747.4 Z"/>
    <path class="pie-slice" fill="var(--slice-deepblue)" d="M622 472 L727.7 747.4 A295 295 0 0 1 344.8 572.9 Z"/>
    <path class="pie-slice" fill="var(--slice-darkgray)" d="M622 472 L344.8 572.9 A295 295 0 0 1 452.8 230.3 Z"/>
    <path class="pie-slice" fill="var(--slice-midgray)" d="M622 472 L452.8 230.3 A295 295 0 0 1 622 177 Z"/>

    <text class="slice-label label-light" x="566" y="261">Lorem<tspan x="566" dy="31">ipsum</tspan><tspan x="566" dy="31">dolor</tspan></text>
    <text class="slice-label label-dark" x="680" y="261">Lorem<tspan x="680" dy="31">ipsum</tspan><tspan x="680" dy="31">dolor</tspan></text>
    <text class="slice-label label-dark" x="800" y="430">Lorem ipsum<tspan x="800" dy="31">dolor</tspan></text>
    <text class="slice-label label-dark" x="761" y="592">Lorem ipsum<tspan x="761" dy="31">dolor</tspan></text>
    <text class="slice-label label-dark" x="540" y="610">Lorem ipsum dolor<tspan x="540" dy="31">Lorem ipsum dolor</tspan></text>
    <text class="slice-label label-light" x="456" y="421">Lorem ipsum dolor<tspan x="456" dy="31">Lorem ipsum dolor</tspan></text>

    <circle cx="622" cy="472" r="39" fill="var(--hub-blue)" stroke="var(--white)" stroke-width="3"/>
  </svg>

  <footer class="slide-footer">
    <span class="footer-brand">TRV</span>
    <span class="copyright">Copyright text here</span>
    <span class="page-number">01</span>
  </footer>
</main>
</body>
</html>
```